Bussiness Card- KU Architects

We are seeking a new business for our practice. We produce innovative architecture for our clients in the field of education, community servise, residential and the retail sector.
We would like to use our new logo attached. Borrow from old card where suitable eg the back section.
Our old card is attached.

Our Updated Contact Details are:
KU Architects. ABN 57 614 302 948
T: 07 3498 2260 F:07 3815 4027 M: 0452 718 904
47 Marrow Street, Ashford Ridge, Queensland 4172
kuarchitects@fernmail.com.au
www.kuarchitects.net.au

Our new logo is attached
The final design should communicate an innovative practice, professional service and a commitment to quality

Target Market(s)

Education Client
Corporate Clients
Community Organisations

Industry/Entity Type

Professional Service

```html
<!DOCTYPE html>
<html lang="en">
<head>
<meta charset="utf-8">
<title>KU Architects — Business Card</title>
<link rel="stylesheet" href="https://fonts.googleapis.com/css2?family=Oswald:wght@400;600&family=Arimo:wght@400;700&display=swap">
<style>
  :root {
    --stage: #f2f4f4;
    --card: #3e494b;
    --lime: #7fe016;
    --muted: #8a9496;
    --shadow: rgba(0, 0, 0, 0.18);
  }
  html, body {
    margin: 0;
    padding: 0;
    width: 1200px;
    height: 707px;
    overflow: hidden;
    background: var(--stage);
  }
  .stage {
    position: relative;
    width: 1200px;
    height: 707px;
  }
  .card {
    position: absolute;
    top: 203px;
    width: 525px;
    height: 300px;
    background: var(--card);
    box-shadow: 0 6px 18px var(--shadow);
    overflow: hidden;
  }
  .card--front { left: 50px; }
  .card--back { left: 625px; }

  /* Front */
  .accent-bar {
    position: absolute;
    left: 0;
    top: 30px;
    width: 240px;
    height: 22px;
    background: var(--lime);
  }
  .identity {
    position: absolute;
    right: 34px;
    top: 30px;
    text-align: right;
  }
  .identity__name {
    display: flex;
    align-items: center;
    justify-content: flex-end;
    gap: 8px;
    height: 32px;
    font-family: "Oswald", sans-serif;
    font-weight: 600;
    font-size: 30px;
    line-height: 1;
    letter-spacing: 0.5px;
    color: var(--lime);
    text-transform: uppercase;
  }
  .identity__square {
    width: 22px;
    height: 22px;
    background: var(--lime);
    flex: none;
  }
  .identity__full {
    margin-top: 6px;
    font-family: "Oswald", sans-serif;
    font-weight: 400;
    font-size: 10px;
    letter-spacing: 4.6px;
    color: var(--muted);
    text-transform: uppercase;
  }
  .identity__tagline {
    margin-top: 2px;
    font-family: "Oswald", sans-serif;
    font-weight: 400;
    font-size: 13px;
    letter-spacing: 2px;
    color: var(--muted);
    text-transform: uppercase;
  }
  .contact {
    position: absolute;
    right: 34px;
    top: 128px;
    text-align: right;
    font-family: "Arimo", sans-serif;
    color: var(--lime);
    font-size: 12px;
    line-height: 1.45;
  }
  .contact__person {
    font-weight: 700;
    font-size: 16px;
    line-height: 1.2;
  }
  .contact__quals { font-size: 10.5px; margin-bottom: 4px; }
  .contact__firm { font-weight: 700; }
  .contact__email {
    position: absolute;
    left: 40px;
    bottom: 34px;
    font-family: "Arimo", sans-serif;
    font-size: 12px;
    color: var(--lime);
  }

  /* Back */
  .back-field {
    position: absolute;
    right: 0;
    top: 0;
    width: 235px;
    height: 300px;
    background: var(--lime);
  }
  .back-identity {
    position: absolute;
    left: 36px;
    top: 96px;
    font-family: "Oswald", sans-serif;
    color: var(--muted);
    text-transform: uppercase;
  }
  .back-identity__full {
    font-size: 9px;
    letter-spacing: 4.4px;
  }
  .back-identity__tagline {
    margin-top: 3px;
    font-size: 12px;
    letter-spacing: 2px;
  }
  .web {
    position: absolute;
    left: 36px;
    bottom: 82px;
    font-family: "Arimo", sans-serif;
    font-size: 12px;
    color: var(--lime);
  }
</style>
</head>
<body>
<main class="stage">

  <section class="card card--front" aria-label="Business card front">
    <div class="accent-bar"></div>
    <div class="identity">
      <div class="identity__name"><span class="identity__square"></span>KU Architects</div>
      <div class="identity__full">Kaito Ulmer Architects</div>
      <div class="identity__tagline">Designing Together</div>
    </div>
    <div class="contact">
      <div class="contact__person">Kaito Ulmer</div>
      <div class="contact__quals">B Arch(melb) B Planning(melb)</div>
      <div class="contact__firm">KU ARCHITECTS. ABN 57 614 302 948</div>
      <div>T: 07 3498 2260&nbsp;&nbsp;F: 07 3815 4027&nbsp;&nbsp;M: 0452 718 904</div>
      <div>47 Marrow Street, Ashford Ridge, Queensland 4172</div>
    </div>
    <div class="contact__email">kuarchitects@fernmail.com.au</div>
  </section>

  <section class="card card--back" aria-label="Business card back">
    <div class="back-identity">
      <div class="back-identity__full">Kaito Ulmer Architects</div>
      <div class="back-identity__tagline">Designing Together</div>
    </div>
    <div class="web">www.kuarchitects.net.au</div>
    <div class="back-field"></div>
  </section>

</main>
</body>
</html>
```